Webdesign für Immobilienmakler / Immobilienbüro
Zielgruppe
Das Unternehmen heißt LUMAR GmbH und kommt aus Heerbrugg in der Schweiz und will nun den Bereich Immobilien Vermarktung, Verkauf, Vermietung auf Süddeutschland erweitern.
Wir haben bis heute keine Webseite, weil unser Geschäft bis dato in der Schweiz durch Empfehlung, Mundpropaganda und Zeitunganzeigen funktioniert hat. Aber in Deutschland ist es ja ein Muß, was uns sicherlich auch den Einstieg erleichtern wird.
Aufgabenstellung
Wir benötigen eine Homepage für den Verkauf, Vermietung, Vermittlung von Immobilien für Privat und Gewerbe. Zu den Kategorien und der Gliederung haben wir keine bestimmte Vorstellung.
Hier hat der Designer freie Hand und wir freuen uns auf Ihren Vorschlag

```html
<!DOCTYPE html>
<html lang="de">
<head>
<meta charset="utf-8">
<title>LUMAR GmbH – Immobilien</title>
<link href="https://fonts.googleapis.com/css2?family=Arimo:wght@400;700&display=swap" rel="stylesheet">
<style>
:root{
  --brown:#7b3200;
  --brown-dark:#6a2a00;
  --panel-brown:#b08a74;
  --text:#555;
  --text-dark:#444;
  --page:#dadada;
  --panel:#ebebeb;
  --card:#f5f5f5;
  --field:#fff;
}
*{box-sizing:border-box;margin:0;padding:0}
html,body{width:1024px;height:1200px;overflow:hidden}
body{background:var(--page);font-family:"Arimo",Arial,sans-serif;color:var(--text);position:relative;font-size:10px}
a{color:inherit;text-decoration:none}
.abs{position:absolute}
.brand{left:116px;top:12px;font-size:33px;color:var(--brown);letter-spacing:-.3px}
.meta-links{right:109px;font-size:10px;color:#666}
.meta-links.top{top:33px}
.hero{left:116px;top:50px;width:792px;height:400px;background:linear-gradient(135deg,#c9a77a 0%,#b48b5c 35%,#6d89ab 55%,#d9b488 80%,#c59c6a 100%)}
.hero-caption{position:absolute;left:478px;top:49px;width:312px;height:119px;background:rgba(250,246,240,.88);padding:10px 11px}
.hero-caption h1{font-weight:400;font-size:16px;line-height:20px;color:var(--brown)}
.hero-caption p{margin-top:14px;font-size:9px;line-height:12px;color:#555}
.more{color:var(--brown);display:inline-flex;align-items:center;gap:4px}
.more svg{width:12px;height:8px}
.hero-caption .more{position:absolute;right:11px;bottom:6px;font-size:9.5px}
.dots{position:absolute;left:362px;top:380px;display:flex;gap:3px}
.dots span{width:12px;height:12px;border-radius:50%;background:#e6e6e6;border:2px solid #bbb}
.dots span.on{background:var(--brown)}
.nav{left:116px;top:463px;width:792px;height:28px;background:var(--panel);display:flex;align-items:center;font-size:13px;color:#555}
.nav a{padding:0 8px}
.nav a.active{background:#fff;color:var(--brown);height:28px;line-height:28px;padding:0 9px}
.nav .sep{color:#555}
.social{margin-left:auto;margin-right:9px;display:flex;gap:6px}
.social span{width:20px;height:20px;background:#9a7a66}
.panel{background:var(--panel)}
.main{left:116px;top:504px;width:792px;height:266px}
.card{top:525px;width:176px;height:221px;background:var(--card);padding:11px 12px}
.card .img{width:149px;height:98px;position:relative}
.card h3{margin-top:7px;font-weight:400;font-size:12.5px;color:var(--brown)}
.card .loc{font-size:9.5px;color:var(--brown)}
.card ul{list-style:none;margin-top:12px;font-size:9.5px;line-height:12px;color:#555}
.card .more{position:absolute;right:15px;bottom:8px;font-size:9.5px}
.plus{position:absolute;right:6px;top:6px;width:14px;height:14px}
.badge{position:absolute;left:-3px;top:-3px;width:30px;height:30px}
.sell{left:116px;top:781px;width:792px;height:83px}
.sell .img{position:absolute;left:10px;top:9px;width:176px;height:63px;background:linear-gradient(90deg,#4d7a35,#c6b092 35%,#c7b08e 70%,#5d8a3b)}
.sell h2{position:absolute;left:209px;top:13px;font-weight:400;font-size:12.5px;color:var(--brown)}
.sell p{position:absolute;left:209px;top:42px;font-size:10px;line-height:13px;color:#555}
.search{left:722px;top:525px;width:176px;height:345px;background:var(--panel-brown);box-shadow:0 2px 4px rgba(0,0,0,.25)}
.search-head{position:absolute;left:-5px;top:11px;width:186px;height:22px;background:var(--brown);color:#fff;font-size:12.5px;line-height:22px;padding-left:16px}
.field{position:absolute;background:var(--field);height:17px;font-size:10px;color:#666;line-height:17px;padding-left:5px}
.field.sel::after{content:"»";position:absolute;right:6px;top:0;transform:rotate(90deg);font-size:10px}
.lbl{position:absolute;font-size:10px;color:#fff}
.go{position:absolute;left:11px;top:304px;width:155px;height:25px;background:var(--brown);border-radius:4px;color:#fff;font-size:12px;display:flex;align-items:center;justify-content:center;gap:6px}
.go svg{width:13px;height:9px}
.news{left:116px;top:875px;width:385px;height:218px;padding:15px 10px 0 10px}
.week{left:523px;top:875px;width:385px;height:218px;padding:15px 12px}
.box-title{font-weight:400;font-size:12.5px;color:var(--brown)}
.rss{position:absolute;right:8px;top:6px;width:20px;height:20px;background:#e8792b}
.item{position:relative;margin-top:14px;font-size:9.8px;line-height:13.2px;color:#555;width:360px}
.news .box-title+.item{margin-top:17px}
.item b{color:#555}
.item .more{position:absolute;right:15px;bottom:0;font-size:9.8px}
.news .older{position:absolute;left:10px;bottom:12px;font-size:9.8px}
.week p{width:170px;margin-top:14px;font-size:10px;line-height:13px;color:#555}
.week .more{position:absolute;left:12px;bottom:11px;font-size:10px}
.week .img{position:absolute;left:199px;top:14px;width:176px;height:192px;background:linear-gradient(180deg,#d8d2c4 0%,#c8bfae 55%,#b88e5e 100%)}
.footer-line{left:116px;top:1116px;width:792px;height:1px;background:#9b5b34}
.copyright{left:125px;top:1128px;font-size:10px;color:#666}
.meta-links.bottom{top:1128px}
</style>
</head>
<body>

<div class="abs brand">LUMAR GmbH</div>
<div class="abs meta-links top"><a href="#">AGB</a> | <a href="#">Downloads</a> | <a href="#">Impressum</a></div>

<section class="abs hero" role="img" aria-label="Foto: junges Paar sitzt lachend zwischen Umzugskartons mit Sektgläsern">
  <div class="hero-caption">
    <h1>Schnell im neuen Zuhause wohlfühlen -<br>ganz stressfrei!</h1>
    <p>Lorem ipsum dolor sit amet, consetetur sadipscing elitr, sed diam nonumy eirmod tempor invidunt ut labore et dolore magna aliquyam erat, sed diam voluptua.</p>
    <a class="more" href="#"><svg viewBox="0 0 12 8"><path d="M0 2h6V0l6 4-6 4V6H0z" fill="#7b3200"/></svg>Mehr erfahren</a>
  </div>
  <div class="dots"><span class="on"></span><span></span><span></span><span></span><span></span></div>
</section>

<nav class="abs nav">
  <a class="active" href="#">Startseite</a><span class="sep">|</span>
  <a href="#">Über uns</a><span class="sep">|</span>
  <a href="#">Immobilien für Privat</a><span class="sep">|</span>
  <a href="#">Gewerbeimmobilien</a><span class="sep">|</span>
  <a href="#">Kontakt</a>
  <div class="social" aria-label="Soziale Netzwerke"><span></span><span></span><span></span></div>
</nav>

<div class="abs panel main"></div>

<article class="abs card" style="left:126px">
  <div class="img" role="img" aria-label="Foto: gelbes Einfamilienhaus mit Garten" style="background:linear-gradient(180deg,#2d5fa8 0%,#3e73b8 40%,#d2a94f 60%,#4f7a2e 100%)">
    <svg class="badge" viewBox="0 0 30 30"><path d="M0 0h30L0 30z" fill="#7b3200"/><text x="4" y="18" transform="rotate(-45 9 14)" font-family="Arimo,sans-serif" font-size="7" fill="#fff">NEU</text></svg>
    <svg class="plus" viewBox="0 0 14 14"><circle cx="7" cy="7" r="6" fill="none" stroke="#fff" stroke-width="1.4"/><path d="M7 4v6M4 7h6" stroke="#fff" stroke-width="1.4"/></svg>
  </div>
  <h3>Einfamilienhaus (Kauf)</h3>
  <div class="loc">in Stuttgart (BW)</div>
  <ul><li>120m² Wohnfläche</li><li>250m² Grundstück</li><li>4 Zimmer, Küche, 2 Bäder</li></ul>
  <a class="more" href="#"><svg viewBox="0 0 12 8"><path d="M0 2h6V0l6 4-6 4V6H0z" fill="#7b3200"/></svg>Weitere Informationen</a>
</article>

<article class="abs card" style="left:325px">
  <div class="img" role="img" aria-label="Foto: helles Wohnzimmer mit weißem Sofa und roten Kissen" style="background:linear-gradient(180deg,#e5e5e5 0%,#d9d4cc 50%,#b9874f 100%)">
    <svg class="plus" viewBox="0 0 14 14"><circle cx="7" cy="7" r="6" fill="none" stroke="#fff" stroke-width="1.4"/><path d="M7 4v6M4 7h6" stroke="#fff" stroke-width="1.4"/></svg>
  </div>
  <h3>4-Zimmer-Wohnung (Miete)</h3>
  <div class="loc">in Stuttgart (BW)</div>
  <ul><li>120m² Wohnfläche</li><li>250m² Grundstück</li><li>4 Zimmer, Küche, 2 Bäder</li></ul>
  <a class="more" href="#"><svg viewBox="0 0 12 8"><path d="M0 2h6V0l6 4-6 4V6H0z" fill="#7b3200"/></svg>Weitere Informationen</a>
</article>

<article class="abs card" style="left:523px">
  <div class="img" role="img" aria-label="Foto: modernes weißes Bürogebäude mit Außentreppe" style="background:linear-gradient(180deg,#4a7fc4 0%,#8fb5e0 45%,#e8e8e8 60%,#9a9a9a 100%)">
    <svg class="plus" viewBox="0 0 14 14"><circle cx="7" cy="7" r="6" fill="none" stroke="#fff" stroke-width="1.4"/><path d="M7 4v6M4 7h6" stroke="#fff" stroke-width="1.4"/></svg>
  </div>
  <h3>Gewerbeimmobilie (Miete)</h3>
  <div class="loc">in Stuttgart (BW)</div>
  <ul><li>120m² Wohnfläche</li><li>250m² Grundstück</li><li>4 Zimmer, Küche, 2 Bäder</li></ul>
  <a class="more" href="#"><svg viewBox="0 0 12 8"><path d="M0 2h6V0l6 4-6 4V6H0z" fill="#7b3200"/></svg>Weitere Informationen</a>
</article>

<section class="abs panel sell">
  <div class="img" role="img" aria-label="Foto: Holzschild mit der Aufschrift Baugrund zu verkaufen auf einer Wiese"></div>
  <h2>Sie möchten Ihre Immobilie verkaufen oder vermieten?</h2>
  <p>Wir sind ständig auf der Suche nach neuen Objekten!<br>Treten Sie einfach mit uns in Kontakt:</p>
</section>

<aside class="abs search">
  <div class="search-head">Immobiliensuche:</div>
  <div class="field sel" style="left:11px;top:48px;width:155px">Gewerbeimmobilien</div>
  <div class="field sel" style="left:11px;top:72px;width:155px">Zur Miete</div>
  <div class="field" style="left:11px;top:96px;width:155px">Ort</div>
  <div class="lbl" style="left:10px;top:130px">Umkreis:</div>
  <div class="field sel" style="left:88px;top:121px;width:78px">Bis 10km</div>
  <div class="lbl" style="left:11px;top:150px">Anzahl der Zimmer:</div>
  <div class="lbl" style="left:11px;top:167px">von:</div><div class="field" style="left:38px;top:164px;width:38px"></div>
  <div class="lbl" style="left:104px;top:167px">bis:</div><div class="field" style="left:129px;top:164px;width:37px"></div>
  <div class="lbl" style="left:11px;top:200px">Wohnfläche in m²:</div>
  <div class="lbl" style="left:11px;top:217px">von:</div><div class="field" style="left:38px;top:214px;width:38px"></div>
  <div class="lbl" style="left:104px;top:217px">bis:</div><div class="field" style="left:129px;top:214px;width:37px"></div>
  <div class="lbl" style="left:11px;top:250px">Preis:</div>
  <div class="lbl" style="left:11px;top:267px">von:</div><div class="field" style="left:38px;top:264px;width:38px"></div>
  <div class="lbl" style="left:104px;top:267px">bis:</div><div class="field" style="left:129px;top:264px;width:37px"></div>
  <a class="go" href="#"><svg viewBox="0 0 12 8"><path d="M0 2h6V0l6 4-6 4V6H0z" fill="#fff"/></svg>Jetzt Suche starten</a>
</aside>

<section class="abs panel news">
  <h2 class="box-title">Aktuelle Neuigkeiten:</h2>
  <span class="rss" aria-label="Newsfeed"></span>
  <div class="item"><b>01.02.13: Lorem Ipsum dolor sit amet:</b> Lorem ipsum dolor sit amet, conse-tetur sadipscing elitr, sed diam nonumy eirmod tempor invidunt ut labore et dolore magna aliquyam erat, sed diam voluptua...
    <a class="more" href="#"><svg viewBox="0 0 12 8"><path d="M0 2h6V0l6 4-6 4V6H0z" fill="#7b3200"/></svg>Mehr erfahren</a></div>
  <div class="item"><b>01.02.13: Lorem Ipsum dolor sit amet:</b> Lorem ipsum dolor sit amet, conse-tetur sadipscing elitr, sed diam nonumy eirmod tempor invidunt ut labore et dolore magna aliquyam erat, sed diam voluptua...
    <a class="more" href="#"><svg viewBox="0 0 12 8"><path d="M0 2h6V0l6 4-6 4V6H0z" fill="#7b3200"/></svg>Mehr erfahren</a></div>
  <div class="item"><b>01.02.13: Lorem Ipsum dolor sit amet:</b> Lorem ipsum dolor sit amet, conse-tetur sadipscing elitr, sed diam nonumy eirmod tempor invidunt ut labore et dolore magna aliquyam erat, sed diam voluptua...
    <a class="more" href="#"><svg viewBox="0 0 12 8"><path d="M0 2h6V0l6 4-6 4V6H0z" fill="#7b3200"/></svg>Mehr erfahren</a></div>
  <a class="more older" href="#"><svg viewBox="0 0 12 8"><path d="M0 2h6V0l6 4-6 4V6H0z" fill="#7b3200"/></svg>Ältere Neuigkeiten</a>
</section>

<section class="abs panel week">
  <h2 class="box-title">Immobilie der Woche:</h2>
  <p>Lorem ipsum dolor sit amet, con-setetur sadipscing elitr, sed diam nonumy eirmod tempor invidunt ut labore et dolore magna aliquyam erat, sed diam voluptua.</p>
  <p>Lorem ipsum dolor sit amet, con-setetur sadipscing elitr, sed diam nonumy eirmod tempor invidunt ut labore. Lorem ipsum dolor sit amet.</p>
  <a class="more" href="#"><svg viewBox="0 0 12 8"><path d="M0 2h6V0l6 4-6 4V6H0z" fill="#7b3200"/></svg>Mehr erfahren</a>
  <div class="img" role="img" aria-label="Foto: modernes Wohnzimmer mit gelbem Sofa, weißem Teppich und Holzboden">
    <svg class="plus" viewBox="0 0 14 14"><circle cx="7" cy="7" r="6" fill="none" stroke="#fff" stroke-width="1.4"/><path d="M7 4v6M4 7h6" stroke="#fff" stroke-width="1.4"/></svg>
  </div>
</section>

<div class="abs footer-line"></div>
<div class="abs copyright">Copyright 2013: LUMAR GmbH</div>
<div class="abs meta-links bottom"><a href="#">AGB</a> | <a href="#">Downloads</a> | <a href="#">Impressum</a></div>

</body>
</html>
```